Bref créative
FXK-TWO Business Cards and Stationery
Paintless Dent Repair
Modern
Calvin t Moss
Owner-Technician
4172 Salvia ln
riverside ca 91734
glowmenderfxk7@mailvista.example
repair dings dents hail damage
20 years experience master craftsman

```html
<!DOCTYPE html>
<html lang="en">
<head>
<meta charset="utf-8">
<title>FXK-TWO Business Cards</title>
<link href="https://fonts.googleapis.com/css2?family=Open+Sans:wght@400;600&display=swap" rel="stylesheet">
<style>
  :root {
    --bg: #d6d7d9;
    --card: #ffffff;
    --red: #d81f26;
    --navy: #2a3f7a;
    --ink: #333333;
    --muted: #777777;
    --rule: #c9c9c9;
  }
  * { box-sizing: border-box; margin: 0; padding: 0; }
  html, body { width: 1200px; height: 895px; overflow: hidden; }
  body {
    background: var(--bg);
    font-family: "Open Sans", Arial, sans-serif;
    position: relative;
  }
  .card {
    position: absolute;
    left: 250px;
    width: 700px;
    height: 400px;
    background: var(--card);
    box-shadow: 0 6px 18px rgba(0,0,0,.18);
  }
  .card--back { top: 27px; }
  .card--front { top: 467px; }

  .band { position: absolute; left: 0; right: 0; height: 16px; background: var(--red); }
  .band--top { top: 0; border-bottom: 3px solid var(--navy); }
  .band--bottom { bottom: 0; border-top: 3px solid var(--navy); }

  .brand { position: absolute; left: 0; right: 0; text-align: center; }
  .brand__name {
    display: inline-flex;
    align-items: center;
    gap: 12px;
    font-weight: 600;
    font-size: 40px;
    line-height: 1.1;
    color: var(--red);
  }
  .brand__mark {
    width: 14px;
    height: 14px;
    background: var(--navy);
  }
  .brand__tagline {
    font-weight: 600;
    font-size: 22px;
    color: var(--navy);
    letter-spacing: 1px;
    margin-top: 8px;
  }
  .brand__services {
    font-size: 10px;
    color: var(--muted);
    margin-top: 6px;
  }
  .card--back .brand { top: 115px; }
  .card--front .brand { top: 62px; }

  .web {
    position: absolute;
    right: 120px;
    top: 270px;
    font-size: 20px;
    color: var(--red);
    letter-spacing: 1px;
  }
  .web span { color: var(--navy); }

  .identity {
    position: absolute;
    top: 245px;
    right: 372px;
    text-align: right;
    font-size: 13px;
    line-height: 1.45;
    color: var(--ink);
  }
  .identity__name { color: var(--red); font-size: 15px; font-weight: 600; }
  .identity__role { margin-bottom: 14px; }

  .divider {
    position: absolute;
    left: 350px;
    top: 240px;
    width: 1px;
    height: 120px;
    background: var(--rule);
  }

  .contacts {
    position: absolute;
    left: 368px;
    top: 250px;
    list-style: none;
    font-size: 13px;
    color: var(--ink);
  }
  .contacts li { display: flex; align-items: center; height: 24px; }
  .contacts svg { width: 16px; height: 16px; margin-right: 8px; flex: none; }
</style>
</head>
<body>

<section class="card card--back">
  <div class="band band--top"></div>
  <div class="brand">
    <div class="brand__name"><span class="brand__mark"></span>FXK-TWO</div>
    <div class="brand__tagline">Paintless dent repair</div>
    <div class="brand__services">Hail damage · dings · dents · 20 years master craftsman</div>
  </div>
  <div class="web">www.<span>glowmenderfxk</span>.example</div>
  <div class="band band--bottom"></div>
</section>

<section class="card card--front">
  <div class="band band--top"></div>
  <div class="brand">
    <div class="brand__name"><span class="brand__mark"></span>FXK-TWO</div>
    <div class="brand__tagline">Paintless dent repair</div>
    <div class="brand__services">Hail damage · dings · dents · 20 years master craftsman</div>
  </div>

  <div class="identity">
    <div class="identity__name">Calvin t Moss</div>
    <div class="identity__role">Owner-Technician</div>
    <div>4172 Salvia ln</div>
    <div>riverside ca 91734</div>
  </div>

  <div class="divider"></div>

  <ul class="contacts">
    <li>
      <svg viewBox="0 0 16 16"><circle cx="8" cy="8" r="8" fill="var(--red)"/><path d="M5 4.5l1.6-.5 1 2-1 .8a5 5 0 0 0 2.6 2.6l.8-1 2 1-.5 1.6c-3.5.2-6.7-3-6.5-6.5z" fill="#fff"/></svg>
      951-555-0142
    </li>
    <li>
      <svg viewBox="0 0 16 16"><circle cx="8" cy="8" r="8" fill="var(--red)"/><rect x="4" y="5" width="8" height="6" fill="none" stroke="#fff" stroke-width="1.2"/><path d="M4 5l4 3.5L12 5" fill="none" stroke="#fff" stroke-width="1.2"/></svg>
      glowmenderfxk7@mailvista.example
    </li>
    <li>
      <svg viewBox="0 0 16 16"><circle cx="8" cy="8" r="8" fill="var(--red)"/><circle cx="8" cy="8" r="4" fill="none" stroke="#fff" stroke-width="1.1"/><path d="M4 8h8M8 4c-2 2.2-2 5.8 0 8M8 4c2 2.2 2 5.8 0 8" fill="none" stroke="#fff" stroke-width="0.9"/></svg>
      www.glowmenderfxk.example
    </li>
  </ul>
  <div class="band band--bottom"></div>
</section>

</body>
</html>
```